Realtor/Real Estate Investor Business Card Design

We need a business card design for a new real estate company in Maryland. We buy houses, fix and sell. We do wholesaling as well. We also rent houses.We would like to have blue background and white font.
Updates

Hi All,
I thank all of you for your efforts. You are all experts in designing.
Looking forward to meeting you online in the near future.
mira

Industry/Entity Type

Real Estate

Contact Information for Business Card

Mira Talvek
Real Estate Professional
mira@brightlanehomes.example
301-555-0148
Bright Lane Homes.com

Requirements
Must have
• House picture, and logo at the back of the card
We simplify your buying and selling real estate. at the back of the card

```html
<!DOCTYPE html>
<html lang="en">
<head>
<meta charset="utf-8">
<title>Bright Lane Homes – Business Card</title>
<link rel="stylesheet" href="https://fonts.googleapis.com/css2?family=Roboto+Condensed:wght@700;900&family=Arimo:wght@400;700&display=swap">
<style>
  :root {
    --page-bg: #e9e9eb;
    --card-navy-deep: #050d1c;
    --card-navy: #0f2d52;
    --band-black: #030303;
    --band-blue: #0a5a9a;
    --band-blue-dark: #074274;
    --gold: #e8b820;
    --gold-light: #fbe38a;
    --text-white: #ffffff;
  }
  * { margin: 0; padding: 0; box-sizing: border-box; }
  html, body {
    width: 1200px;
    height: 900px;
    overflow: hidden;
    background: var(--page-bg);
  }
  .business-card {
    position: absolute;
    left: 100px;
    top: 165px;
    width: 1000px;
    height: 570px;
    overflow: hidden;
    background: radial-gradient(ellipse at 50% 45%, var(--card-navy) 0%, #0a1f3c 45%, var(--card-navy-deep) 100%);
    box-shadow: 0 14px 34px rgba(0, 0, 0, 0.28);
  }
  .card-bands {
    position: absolute;
    inset: 0;
    width: 100%;
    height: 100%;
  }
  .company-name {
    position: absolute;
    left: 0;
    width: 100%;
    top: 38px;
    text-align: center;
    font-family: "Roboto Condensed", sans-serif;
    font-weight: 900;
    font-size: 104px;
    line-height: 1;
    color: var(--text-white);
    letter-spacing: -1px;
  }
  .agent {
    position: absolute;
    left: 0;
    width: 100%;
    top: 236px;
    text-align: center;
  }
  .agent-name {
    font-family: "Roboto Condensed", sans-serif;
    font-weight: 700;
    font-size: 54px;
    line-height: 1;
    color: var(--text-white);
  }
  .agent-title {
    margin-top: 6px;
    font-family: "Arimo", sans-serif;
    font-weight: 700;
    font-size: 27px;
    color: var(--gold);
  }
  .contact {
    position: absolute;
    left: 0;
    width: 100%;
    top: 350px;
    text-align: center;
    font-family: "Arimo", sans-serif;
    color: var(--text-white);
  }
  .contact-phone {
    font-weight: 700;
    font-size: 44px;
    line-height: 1.05;
  }
  .contact-email {
    font-weight: 400;
    font-size: 30px;
    line-height: 1.2;
  }
  .website {
    position: absolute;
    left: 0;
    width: 100%;
    top: 512px;
    text-align: center;
    font-family: "Arimo", sans-serif;
    font-weight: 400;
    font-size: 38px;
    line-height: 1.1;
    color: var(--text-white);
  }
</style>
</head>
<body>
  <div class="business-card">
    <svg class="card-bands" viewBox="0 0 1000 570" preserveAspectRatio="none" aria-hidden="true">
      <defs>
        <linearGradient id="gold-sweep" x1="0" y1="0" x2="1" y2="0">
          <stop offset="0" stop-color="var(--gold)" stop-opacity="0"/>
          <stop offset="0.35" stop-color="var(--gold)"/>
          <stop offset="0.55" stop-color="var(--gold-light)"/>
          <stop offset="0.8" stop-color="var(--gold)"/>
          <stop offset="1" stop-color="var(--gold)" stop-opacity="0.2"/>
        </linearGradient>
        <linearGradient id="blue-band" x1="0" y1="0" x2="0" y2="1">
          <stop offset="0" stop-color="var(--band-blue)"/>
          <stop offset="1" stop-color="var(--band-blue-dark)"/>
        </linearGradient>
      </defs>
      <path class="top-band" d="M0 0 H1000 V95 C880 140 720 195 420 205 C250 208 120 200 0 198 Z" fill="var(--band-black)"/>
      <path class="top-gold-line" d="M120 212 C300 222 560 215 720 185 C820 166 900 140 1000 100" fill="none" stroke="url(#gold-sweep)" stroke-width="6" stroke-linecap="round"/>
      <path class="bottom-band" d="M0 528 C350 508 700 472 1000 410 V570 H0 Z" fill="url(#blue-band)"/>
      <path class="bottom-gold-line" d="M0 528 C350 508 700 472 1000 410" fill="none" stroke="url(#gold-sweep)" stroke-width="7"/>
    </svg>

    <div class="company-name">Bright Lane Homes</div>

    <div class="agent">
      <div class="agent-name">Mira Talvek</div>
      <div class="agent-title">Real Estate Professional</div>
    </div>

    <div class="contact">
      <div class="contact-phone">301.555.0148</div>
      <div class="contact-email">mira@brightlanehomes.example</div>
    </div>

    <div class="website">www.BrightLaneHomes.example</div>
  </div>
</body>
</html>
```